Velquor Medspa Home Page Design

I need a home page designed for a medical spa of which there are thousands in the US. Their primary purpose is to enhance personal beauty using non-surgical means, such as laser treatment and micro-needling. Since insurance typically doesn't cover such procedures, we are appealing to a mostly upscale end user, probably about 70% female.

Target Market(s)

Women 35-54

Industry/Entity Type

Medical cosmetics

Number of Pages Required

1 page

Font styles to use
Other font styles liked:
• I want very readable content, even by seniors. No grey copy, please. Black only.

Requirements
Must have
• This needs to be a photo-heavy design. Here's one example among hundreds to illustrate what other practices put forth to attract patients. https://www.plomerivaclinics.com/ Stock photos are fine, though I would prefer they obtained from Pixbarrow since I have an account with them. Finally, for now, I'm looking for a static website, we'll do the coding ourselves. Thank you. r psare
Nice to have
• I would also like you tpo consider staggering the five areas with content and a photo on the home page where the dominant photos are not always on the left or right. I think that help provide somefluidity to the sit's overall appearance. And "smooth" is a key quality as, in mamy cases, that's what attracts patients, i.e., the promise of smoother looking skin. his style: four e
Should not have
• Nice, open layout, but not loose. The home page document I attached contains all home page content and everything you need for the navigation bar.

```html
<!DOCTYPE html>
<html lang="en">
<head>
<meta charset="utf-8">
<title>Velquor Medspa</title>
<link href="https://fonts.googleapis.com/css2?family=Open+Sans:wght@400;600;700&display=swap" rel="stylesheet">
<style>
:root{
  --plum:#2b1222;
  --plum-light:#3a1a2d;
  --field:#3b1a2e;
  --olive:#c2b764;
  --cream:#e3da96;
  --ink:#fbf6e6;
  --pink:#b85a8b;
  --line:#b0a55a;
  --footer-text:#e9d4df;
  --page:#ffffff;
}
*{box-sizing:border-box;margin:0;padding:0}
html,body{width:1200px;height:3977px;overflow:hidden;background:var(--page)}
body{font-family:"Open Sans",sans-serif;color:var(--ink)}
.site{position:absolute;left:141px;top:5px;width:918px;height:3972px;background:var(--plum)}
.abs{position:absolute}

/* header */
.brand{left:50px;top:24px;font-weight:700;font-size:22px;color:var(--pink);letter-spacing:1px;white-space:nowrap}
.nav{left:292px;top:32px;display:flex;gap:22px;font-size:10px;color:var(--cream);letter-spacing:.5px}
.phone{left:700px;top:27px;font-size:17px;color:var(--pink);white-space:nowrap}
.phone b{font-size:14px}

/* hero */
.hero-title{left:57px;top:131px;line-height:1.15;font-weight:400}
.hero-title .big{font-size:38px;display:block}
.hero-title .mid{font-size:23px;display:block;margin:2px 0}
.t-olive{color:var(--olive)}
.t-pink{color:var(--pink)}
.t-cream{color:var(--cream)}
.hero-dot{left:54px;top:378px;width:7px;height:7px;border-radius:50%;background:#f0d000}
.btn-solid{left:50px;top:409px;width:114px;height:40px;border-radius:20px;background:#5a2a45;color:var(--ink);font-size:13px;display:flex;align-items:center;justify-content:center}
.hero-photo{left:482px;top:75px;width:436px;height:492px;clip-path:polygon(14% 0,100% 0,100% 100%,0 100%);background:linear-gradient(135deg,#4a2a1c 0%,#8a5a3a 40%,#e4d8cc 70%,#b24060 100%)}

/* about */
.about{left:43px;top:612px;width:830px}
.h-section{font-size:16px;letter-spacing:2px;font-weight:600;color:var(--olive)}
.copy{font-size:12.5px;line-height:1.65;color:var(--ink)}
.about .copy{margin-top:10px}
.btn-line{display:inline-flex;align-items:center;justify-content:center;border:1.5px solid var(--olive);border-radius:16px;height:26px;padding:0 36px;font-size:9px;letter-spacing:1.5px;color:var(--ink)}
.about .btn-line{margin-top:10px;height:24px}

/* feature rows */
.feature{left:0;width:918px;height:494px}
.photo-left{left:0;top:0;width:380px;height:494px;clip-path:polygon(0 0,100% 0,84% 100%,0 100%)}
.photo-right{right:0;top:0;width:382px;height:494px;clip-path:polygon(16% 0,100% 0,100% 100%,0 100%)}
.text-right{left:431px;width:445px}
.text-left{left:45px;width:445px;text-align:right}
.text-left .copy{text-align:left}
.feature .copy{margin-top:20px}
.feature .btn-line{margin-top:20px;height:34px;padding:0 27px;font-size:10.5px}
.ph-inject{background:linear-gradient(120deg,#d9d3c9 0%,#e8cdb8 45%,#b28c62 100%)}
.ph-laser{background:linear-gradient(160deg,#ece7e2 0%,#d8b39c 50%,#f4f1ee 100%)}
.ph-micro{background:linear-gradient(120deg,#dcd7d0 0%,#e5c2aa 50%,#c99a7c 100%)}
.ph-peel{background:linear-gradient(150deg,#eeeae6 0%,#e3bfa6 55%,#f5f2ef 100%)}

/* consultation */
.consult{left:126px;top:2828px;width:665px;text-align:center}
.consult .h-section{font-size:13px}
.consult .copy{margin-top:14px;text-align:left;font-size:12px}
.form{margin-top:20px;display:grid;grid-template-columns:1fr 1fr;gap:7px 12px;text-align:left}
.field{height:28px;border:1px solid var(--line);background:var(--field);font-size:11px;color:var(--ink);padding:0 8px;display:flex;align-items:center;justify-content:space-between}
.field.message{height:54px;align-items:flex-start;padding-top:7px}
.consent{margin-top:22px;font-size:10px;color:var(--ink);display:flex;justify-content:center;align-items:center;gap:6px}
.consent i{width:10px;height:10px;background:#fff;display:inline-block}
.consult .btn-line{margin-top:30px;height:34px;padding:0 28px;font-size:10.5px}

/* contact */
.contact{left:0;top:3275px;width:918px;text-align:center}
.contact .brand-big{font-size:60px;font-weight:700;color:var(--pink);letter-spacing:2px;line-height:1.1}
.contact .addr{margin-top:40px;font-size:13px;line-height:1.8;color:var(--ink)}
.contact .tel{font-size:30px;color:var(--olive)}

/* map */
.map{left:0;top:3574px;width:918px;height:159px;background:linear-gradient(90deg,#b7dcc2 0%,#c9e5d0 45%,#9fc8e8 52%,#c3e2cc 60%,#b7dcc2 100%)}

/* footer */
.footer{left:0;top:3733px;width:918px;height:239px;background:var(--plum-light)}
.fcol{top:30px;width:220px;text-align:center;font-size:10.5px;line-height:19px;color:var(--footer-text)}
.fcol h4{font-weight:600;font-size:10.5px;color:var(--cream);letter-spacing:.5px;margin-bottom:10px}
.fcol .gap{margin-top:10px}
.copyright{left:0;width:918px;top:218px;text-align:center;font-size:9px;color:var(--footer-text)}
</style>
</head>
<body>
<div class="site">
  <div class="abs brand">VELQUOR MEDSPA</div>
  <nav class="abs nav"><span>ABOUT US</span><span>INJECTABLES</span><span>LASER</span><span>MICRO</span><span>OTHER</span><span>CONTACT</span></nav>
  <div class="abs phone">phone | <b>860-555-0182</b></div>

  <h1 class="abs hero-title">
    <span class="big t-olive">THE</span>
    <span class="big t-pink">NON-SURGICAL</span>
    <span class="mid t-olive">APPROACH TO A</span>
    <span class="big t-cream">CONFIDENT YOU</span>
  </h1>
  <div class="abs hero-dot"></div>
  <div class="abs btn-solid">Get started</div>
  <div class="abs hero-photo" role="img" aria-label="Spa still life with candles, bath salts, towels and blossoms"></div>

  <section class="abs about">
    <h2 class="h-section">ABOUT US</h2>
    <p class="copy">Established by Dr. Renna Holloway, M.D., F.A.C.S., Velquor MedSpa employs the latest in nonsurgical cosmetic innovations to enhance your appearance and the way you feel about yourself. All Velquor procedures are non-surgical as we effect healthier, younger-looking skin, facial reshaping, scar and hair removal, numerous other results. Have concerns? Contact us now so we can help put your mind at ease. That's the essence of Velquor.</p>
    <span class="btn-line">LEARN MORE</span>
  </section>

  <section class="abs feature" style="top:790px">
    <div class="abs photo-left ph-inject" role="img" aria-label="Woman with facial mapping lines holding a syringe"></div>
    <div class="abs text-right" style="top:160px">
      <h2 class="h-section">INJECTABLES</h2>
      <p class="copy">Injectables (also known as dermal fillers) are gel-like substances we use to restore lost volume, smooth out wrinkles, and eliminate or soften facial lines. More than one million men and women per year seek injectable treatments to smooth out their chins, enhance or restore volume to sagging cheeks, or plump up their lips. Injectables also can help improve facial symmetry.</p>
      <span class="btn-line">READ MORE</span>
    </div>
  </section>

  <section class="abs feature" style="top:1284px">
    <div class="abs photo-right ph-laser" role="img" aria-label="Woman receiving a laser skin treatment"></div>
    <div class="abs text-left" style="top:160px">
      <h2 class="h-section">LASER TREATMENTS</h2>
      <p class="copy">Velquor Medspa offers numerous laser-based treatments to enhance your personal appearance and boost your self-confidence. We have the right laser treatment option to remove hair and tattoos, tighten your skin, reduce stretch marks, and eliminate blemishes red spots. Plagued by rosacea, acne scars, or even keloids? We have the right treatment plan for you, too.</p>
      <span class="btn-line">READ MORE</span>
    </div>
  </section>

  <section class="abs feature" style="top:1778px">
    <div class="abs photo-left ph-micro" role="img" aria-label="Woman with smooth skin and hexagonal skin detail insets"></div>
    <div class="abs text-right" style="top:170px">
      <h2 class="h-section">MICRO-NEEDLING WITH PRP</h2>
      <p class="copy">Microneedling is a proven effective means to induce the regrowth of collagen. As we age, collagen production naturally declines, thus contributing to skin wrinkling and sagging. Velquor can help reverse that trend with microneedling and PRP (platelet rich plasma) injections combined.</p>
      <span class="btn-line">READ MORE</span>
    </div>
  </section>

  <section class="abs feature" style="top:2272px">
    <div class="abs photo-right ph-peel" role="img" aria-label="Woman relaxing with a facial peel mask"></div>
    <div class="abs text-left" style="top:165px">
      <h2 class="h-section">OTHER TREATMENT OPTIONS</h2>
      <p class="copy">Using a process called chemical peeling, Velquor can remove the top layers of skin so healthier looking skin can grow back in its place. A chemical peel is an effective and popular way to treat wrinkles, and scars. Many patients also find a chemical peel the ideal solution to repair sun damage and address other skin issues.</p>
      <span class="btn-line">READ MORE</span>
    </div>
  </section>

  <section class="abs consult">
    <h2 class="h-section">SCHEDULE YOUR FREE CONSULTATION</h2>
    <p class="copy">Why wonder if you're a candidate for our services when you can so easily find out for yourself? Simply complete and submit this form and a member of our medical team will contact you to schedule your visit. We'll listen to your concerns, answer your questions, and recommend the best strategy for improving how you look and feel about yourself. That's the Velquor way.</p>
    <div class="form">
      <div class="field">First Name *</div>
      <div class="field">Last Name *</div>
      <div class="field">Phone *</div>
      <div class="field">Email *</div>
      <div class="field">City *</div>
      <div class="field">How did you here about Velquor ?
        <svg width="9" height="6" viewBox="0 0 9 6"><path d="M1 1l3.5 3.5L8 1" fill="none" stroke="#fbf6e6" stroke-width="1"/></svg>
      </div>
      <div class="field message">massage</div>
    </div>
    <div class="consent"><i></i>I accept the Terms of Use &amp; agree to receive monthly specials, newsletters, etc. *</div>
    <span class="btn-line">BOOK AN APPOINTMENT</span>
  </section>

  <section class="abs contact">
    <div class="brand-big">VELQUOR MEDSPA</div>
    <p class="addr">4410 Marlow Turnpike<br>Ashcombe CT 06190</p>
    <p class="tel">860-555-0182</p>
  </section>

  <div class="abs map" role="img" aria-label="Street map showing the spa location"></div>

  <footer class="abs footer">
    <div class="abs fcol" style="left:70px">
      <h4>INJECTABLES</h4>
      <div>Neurotox</div><div>Dermafill</div><div>Contoura</div><div>Contoura</div>
    </div>
    <div class="abs fcol" style="left:348px">
      <h4>LASER TREATMENTS</h4>
      <div>Hair Removal</div><div>Tattoo Removal</div><div>Facial Rejuvenation</div><div>Skin Resurfacing</div><div>Scar Treatment</div><div>Stretch Marks</div><div>Other Laser Treatments</div>
    </div>
    <div class="abs fcol" style="left:625px">
      <h4>OTHER TREATMENT OPTIONS</h4>
      <div>Chemical Peels</div><div>Intense Pulsed Light (IPL) Therapy</div>
      <div class="gap">ABOUT US</div><div class="gap">CONTACT</div>
    </div>
    <div class="abs copyright">2024 © copyright</div>
  </footer>
</div>
</body>
</html>
```